Easy - Fix our "Snag the Bash" Promo Flyer

Please see attached promo flyer with all the information required. Looking for quick assistance so we can go live with the advertising for this competition. Looking for something more commercial and polished. Very attractive so that lots of people enter the competition. <br/><br/>Happy for it to look a little bit festive as the competition is running in December. <br/><br/>Attached is out Fork Lodge Logo and first attempts at poster. Please let me know if you need anything further. <br/><br/>If you see any grammar or spelling errors please feel free to fix too.
Target Market(s)
Corporate Businesses who are buying vouchers as staff christmas gifts/bonus
Colors
Designer to choose colors to be used in the design.
Look and feel

```html
<!DOCTYPE html>
<html lang="en">
<head>
<meta charset="utf-8">
<title>Snag the Bash – Fork Lodge Staff Party Flyer</title>
<link href="https://fonts.googleapis.com/css2?family=Kaushan+Script&family=Damion&family=Oswald:wght@400;500;700&family=Open+Sans:wght@400;600;700;800&display=swap" rel="stylesheet">
<style>
  :root {
    --backdrop: #dcdcd8;
    --paper: #ffffff;
    --paper-shade: #efefef;
    --pink: #d9448e;
    --purple: #7b3fb8;
    --blue: #3a3fc0;
    --navy: #1f1a5c;
    --maroon: #8e1b5c;
    --red: #e0202f;
    --ink: #222222;
    --bar: #262626;
    --photo-dark: #26103a;
    --photo-mid: #6e3486;
    --photo-light: #c27aa4;
  }
  * { margin: 0; padding: 0; box-sizing: border-box; }
  html, body { width: 1200px; height: 935px; overflow: hidden; background: var(--backdrop); }
  body { position: relative; font-family: "Open Sans", Arial, sans-serif; color: var(--ink); }

  .flyer {
    position: absolute; left: 290px; top: 19px; width: 620px; height: 897px;
    background: linear-gradient(135deg, var(--paper) 55%, var(--paper-shade) 100%);
    box-shadow: 0 6px 18px rgba(0,0,0,.25);
    overflow: hidden;
  }

  .party-photo { position: absolute; left: 0; top: 0; width: 620px; height: 700px; z-index: 1; }

  .headline { position: absolute; left: 0; top: 0; width: 100%; height: 190px; font-family: "Kaushan Script", cursive; font-weight: 400; z-index: 2; }
  .headline span { position: absolute; white-space: nowrap; line-height: 1; }
  .headline .snag {
    left: 60px; top: 14px; font-size: 76px;
    background: linear-gradient(90deg, var(--pink), var(--purple));
    -webkit-background-clip: text; background-clip: text; color: transparent;
  }
  .headline .ultimate { left: 244px; top: 40px; font-size: 44px; color: var(--purple); }
  .headline .staff { left: 210px; top: 102px; font-size: 48px; color: var(--purple); }
  .headline .bash {
    left: 340px; top: 88px; font-size: 80px;
    background: linear-gradient(90deg, var(--purple), var(--blue));
    -webkit-background-clip: text; background-clip: text; color: transparent;
  }
  .tagline { position: absolute; right: 12px; top: 190px; font-family: "Damion", cursive; font-size: 18px; color: var(--ink); white-space: nowrap; z-index: 2; }

  .date-badge {
    position: absolute; left: 104px; top: 262px; transform: translate(-50%, -50%) rotate(-47deg);
    font-family: "Oswald", sans-serif; font-weight: 700; font-size: 31px; letter-spacing: .5px; white-space: nowrap; z-index: 2;
    background: linear-gradient(90deg, var(--pink), var(--blue));
    -webkit-background-clip: text; background-clip: text; color: transparent;
  }

  .offer {
    position: absolute; left: 388px; top: 560px; transform-origin: 0 100%; transform: rotate(-46deg);
    font-family: "Oswald", sans-serif; line-height: 1; white-space: nowrap; color: var(--ink); z-index: 2;
  }
  .offer p { display: block; }
  .offer .sm { font-size: 8px; font-weight: 500; }
  .offer .amount { font-size: 16px; font-weight: 700; color: var(--blue); }
  .offer .grad {
    background: linear-gradient(90deg, var(--pink), var(--blue));
    -webkit-background-clip: text; background-clip: text; color: transparent;
  }
  .offer .deadline { font-size: 19px; font-weight: 500; }
  .offer .prize { font-size: 28px; font-weight: 700; }
  .offer .guests { padding-left: 135px; }
  .offer .count { font-size: 16px; font-weight: 700; color: var(--pink); }

  .details { position: absolute; left: 0; top: 682px; width: 100%; text-align: center; z-index: 2; }
  .includes { position: absolute; left: 83px; top: 0; font-size: 11.5px; text-transform: uppercase; white-space: nowrap; }
  .hurry { position: absolute; left: 83px; top: 14px; font-size: 10.5px; white-space: nowrap; text-transform: uppercase; }
  .hurry strong { font-size: 17px; font-weight: 800; color: var(--navy); margin-right: 4px; }
  .to-win { position: absolute; left: 352px; top: 10px; font-size: 30px; font-weight: 800; color: var(--maroon); white-space: nowrap; }
  .cake { position: absolute; left: 0; top: 53px; width: 100%; font-size: 8.5px; }
  .xmas { position: absolute; left: 0; top: 66px; width: 100%; font-size: 14px; font-weight: 800; text-transform: uppercase; }
  .xmas em { font-style: normal; color: var(--red); }

  .brand { position: absolute; left: 0; top: 92px; width: 100%; display: flex; justify-content: center; align-items: center; gap: 6px; }
  .brand-dot { width: 12px; height: 12px; border-radius: 50%; background: var(--red); }
  .brand-name { font-family: "Oswald", sans-serif; font-weight: 700; font-size: 20px; color: var(--red); text-transform: uppercase; letter-spacing: 1px; }

  .fine { position: absolute; left: 0; width: 100%; font-size: 8px; font-weight: 700; text-transform: uppercase; }
  .tip { top: 135px; }
  .hr-note { top: 152px; }
  .call-to-action { position: absolute; left: 0; top: 166px; width: 100%; font-size: 8px; font-weight: 700; text-transform: uppercase; }
  .call-to-action i { font-family: "Damion", cursive; font-style: normal; font-size: 17px; text-transform: none; font-weight: 400; margin-right: 3px; }

  .contact-bar {
    position: absolute; left: 0; bottom: 0; width: 100%; height: 20px; background: var(--bar);
    display: flex; align-items: center; justify-content: space-around; padding: 0 40px;
    color: #fff; font-size: 13.5px; font-weight: 600; z-index: 2;
  }
  .contact-item { display: flex; align-items: center; gap: 8px; }
  .contact-icon { width: 14px; height: 14px; background: #fff; border-radius: 2px; display: flex; align-items: center; justify-content: center; }
</style>
</head>
<body>
  <main class="flyer">
    <svg class="party-photo" viewBox="0 0 620 700" role="img" aria-label="Photo of colleagues celebrating with champagne at a party, shown through diagonal rounded stripes">
      <defs>
        <linearGradient id="photoTone" gradientUnits="userSpaceOnUse" x1="80" y1="650" x2="480" y2="230">
          <stop offset="0" stop-color="var(--photo-dark)"/>
          <stop offset=".45" stop-color="var(--photo-mid)"/>
          <stop offset="1" stop-color="var(--photo-light)"/>
        </linearGradient>
      </defs>
      <g stroke="url(#photoTone)" stroke-linecap="round" fill="none">
        <line x1="78" y1="345" x2="185" y2="248" stroke-width="40"/>
        <line x1="140" y1="390" x2="345" y2="235" stroke-width="100"/>
        <line x1="85" y1="485" x2="280" y2="310" stroke-width="60"/>
        <line x1="245" y1="505" x2="465" y2="285" stroke-width="90"/>
        <line x1="110" y1="640" x2="455" y2="415" stroke-width="38"/>
        <line x1="300" y1="590" x2="330" y2="570" stroke-width="26"/>
      </g>
      <circle cx="200" cy="637" r="12" fill="var(--photo-dark)"/>
      <circle cx="195" cy="225" r="11" fill="none" stroke="var(--ink)" stroke-width="1.5"/>
      <circle cx="352" cy="577" r="12" fill="none" stroke="var(--ink)" stroke-width="1.5"/>
    </svg>

    <h1 class="headline" aria-label="Snag the ultimate Staff Bash">
      <span class="snag">Snag</span>
      <span class="ultimate">the ultimate</span>
      <span class="staff">Staff</span>
      <span class="bash">Bash</span>
    </h1>
    <p class="tagline">For you and your colleagues</p>

    <p class="date-badge">DECEMBER 31ST</p>

    <div class="offer">
      <p><span class="sm">PURCHASE </span><span class="amount">K5,000</span><span class="sm"> WORTH OF</span></p>
      <p><span class="sm">VOUCHERS BEFORE </span><span class="deadline grad">DECEMBER 31 ST</span><span class="sm"> AND GO INTO THE DRAW TO WIN</span></p>
      <p><span class="prize grad">ULTIMATE STAFF PARTY</span></p>
      <p class="guests"><span class="sm">FOR </span><span class="count">150</span><span class="sm"> PEOPLE.</span></p>
    </div>

    <section class="details">
      <p class="includes">This includes a venue, BBQ style, PNG menu, roast pig, decor &amp; much more ...</p>
      <p class="hurry"><strong>SO HURRY!</strong>There are only 2 parties</p>
      <p class="to-win">TO WIN</p>
      <p class="cake">We'll even throw in an extra large themed cake with your company logo on it</p>
      <p class="xmas">Have a mighty Xmas at <em>Fork Lodge</em></p>
      <div class="brand"><span class="brand-dot"></span><span class="brand-name">Fork Lodge</span></div>
      <p class="fine tip">Tip: buy more vouchers to have better chances of winning</p>
      <p class="fine hr-note">For every HR department enquiry we receive a special surprise will be given</p>
      <p class="call-to-action"><i>so Hurry up</i> and contact us below on:</p>
    </section>

    <footer class="contact-bar">
      <span class="contact-item">
        <span class="contact-icon"><svg width="10" height="10" viewBox="0 0 24 24"><path d="M6.6 10.8a15 15 0 0 0 6.6 6.6l2.2-2.2c.3-.3.7-.4 1-.2 1.1.4 2.3.6 3.6.6.6 0 1 .4 1 1V20c0 .6-.4 1-1 1A17 17 0 0 1 3 4c0-.6.4-1 1-1h3.5c.6 0 1 .4 1 1 0 1.3.2 2.5.6 3.6.1.3 0 .7-.2 1z" fill="#262626"/></svg></span>
        7040 5588
      </span>
      <span class="contact-item">
        <span class="contact-icon"><svg width="10" height="10" viewBox="0 0 24 24"><rect x="2" y="5" width="20" height="14" rx="1" fill="none" stroke="#262626" stroke-width="2.5"/><path d="M2 6l10 7 10-7" fill="none" stroke="#262626" stroke-width="2.5"/></svg></span>
        sales@forklodgefoods.com
      </span>
      <span class="contact-item">
        <span class="contact-icon"></span>
        forklodge
      </span>
    </footer>
  </main>
</body>
</html>
```